Web Design Project (Mente Lumo)

We are going to do a therapy template to a psychologist. The site already exists, adress: www.mentelumo.net. So, its a total redesign job. I'm from Brazil, the language is PT-BR, so I'm gonna translate what you think be necessary. You can use the current structure from the website as a base to the new design. Check this template to see what I usually like: http://www.layoutkestrel.com/demo/51907.html
Updates

I'm waiting for new creative designs. The 'structure' image is just for 'pb'.

Requirements
Must have
• We need a modern menu, it should use a cool font style and make some kind of effect and little noise when the user pass over with the mouse (FLASH/HTML 5). The main page must emphasize the fact that we offer online treatment, like a picture or frame saying "Online Treatment, click here". It must also show the therapist picture and her name. The colors need to pass a tranquility feeling. The clinic telephone must always be present, doesn't matter which page the user is. The website must adapt to any resolution above 1024x768, crossbrowsing and accept javascript (I'll use www.slotvira.com, so its necessary embed code)
Nice to have
• I would appreciate if there was some kind of slow background animation, passing behind the text using the transparency.
Should not have
• Can't take too long to load, and won't have news or blog

```html
<!DOCTYPE html>
<html lang="en">
<head>
<meta charset="utf-8">
<title>Mente Lumo</title>
<link rel="stylesheet" href="https://fonts.googleapis.com/css2?family=Source+Sans+3:wght@400;600&display=swap">
<style>
  :root {
    --page-top: #fbfbfb;
    --page-bottom: #bfc0c2;
    --brand-blue: #3f6697;
    --panel-green: #a6cc6e;
    --panel-edge: #93b85d;
    --strip-green: #d2e3bc;
    --frame-grey: #b3b4b6;
    --frame-fill: #f3f3f5;
    --ink: #2b2b2b;
    --nav-ink: #ffffff;
  }
  * { box-sizing: border-box; margin: 0; padding: 0; }
  html, body { width: 1200px; height: 900px; overflow: hidden; }
  body {
    position: relative;
    font-family: "Source Sans 3", "Myriad Pro", sans-serif;
    background: linear-gradient(to bottom, var(--page-top) 8%, var(--page-bottom) 100%);
    color: var(--ink);
  }
  .site-header {
    position: absolute; left: 0; top: 0; width: 1200px; height: 60px;
    background: var(--brand-blue);
    box-shadow: 0 2px 5px rgba(0,0,0,0.25);
    display: flex; align-items: center; justify-content: space-between;
    padding: 0 147px;
    color: var(--nav-ink);
  }
  .site-name { font-size: 20px; font-weight: 600; letter-spacing: 0.3px; }
  .clinic-phone { display: flex; align-items: center; gap: 8px; font-size: 17px; }
  .clinic-phone svg { width: 18px; height: 18px; }
  .main-nav {
    position: absolute; left: 147px; top: 199px; width: 906px; height: 51px;
    background: var(--brand-blue);
    box-shadow: 0 2px 5px rgba(0,0,0,0.3);
    display: flex; align-items: center;
    padding: 0 16px 0 15px;
  }
  .main-nav a {
    color: var(--nav-ink); text-decoration: none;
    font-size: 17.5px; font-weight: 400; letter-spacing: 0.2px;
    margin-right: 16px;
  }
  .main-nav .nav-contact { margin-left: auto; margin-right: 0; }
  .panel {
    position: absolute;
    background: var(--panel-green);
    border: 1px solid var(--panel-edge);
    box-shadow: 0 2px 6px rgba(0,0,0,0.28);
  }
  .intro-panel { left: 150px; top: 265px; width: 603px; height: 254px; }
  .portrait-panel { left: 769px; top: 262px; width: 284px; height: 256px; }
  .feature-panel { left: 150px; top: 574px; width: 905px; height: 208px; }
  .feature-strip {
    position: absolute; left: 0; top: 0; width: 100%; height: 30px;
    background: var(--strip-green);
    padding-left: 261px;
    font-size: 15px; font-weight: 600; letter-spacing: 1px; line-height: 30px;
    color: var(--brand-blue);
  }
  .body-copy {
    position: absolute;
    font-size: 17.5px; line-height: 21.7px;
    white-space: nowrap;
  }
  .intro-panel .body-copy { left: 51px; top: 27px; }
  .feature-panel .body-copy { left: 261px; top: 48px; }
  .cta-link { color: var(--brand-blue); font-weight: 600; text-decoration: underline; }
  .photo-frame {
    position: absolute;
    background: var(--frame-fill);
    border: 12px solid var(--frame-grey);
    box-shadow: 2px 3px 6px rgba(0,0,0,0.35);
  }
  .portrait-panel .photo-frame { left: 52px; top: 22px; width: 178px; height: 178px; }
  .therapist-name {
    position: absolute; left: 0; top: 212px; width: 100%;
    text-align: center; font-size: 17.5px; font-weight: 600;
  }
  .therapist-role {
    position: absolute; left: 0; top: 233px; width: 100%;
    text-align: center; font-size: 14px;
  }
  .feature-panel .photo-frame { left: 68px; top: 49px; width: 134px; height: 134px; border-width: 9px; }
</style>
</head>
<body>
  <header class="site-header">
    <span class="site-name">Mente Lumo</span>
    <span class="clinic-phone">
      <svg viewBox="0 0 24 24" aria-hidden="true"><path fill="#ffffff" d="M6.6 10.8a15.1 15.1 0 0 0 6.6 6.6l2.2-2.2a1 1 0 0 1 1-.25 11.4 11.4 0 0 0 3.6.57 1 1 0 0 1 1 1V20a1 1 0 0 1-1 1A17 17 0 0 1 3 4a1 1 0 0 1 1-1h3.5a1 1 0 0 1 1 1c0 1.25.2 2.45.57 3.57a1 1 0 0 1-.25 1z"/></svg>
      (11) 4000-2718
    </span>
  </header>

  <nav class="main-nav">
    <a href="#">HOME</a>
    <a href="#">ABOUT</a>
    <a href="#">ONLINE</a>
    <a href="#" class="nav-contact">CONTACT</a>
  </nav>

  <section class="panel intro-panel">
    <p class="body-copy">Welcome to Mente Lumo, a calm space for care and listening.<br>
    Here you find psychotherapy for adults, couples and teens,<br>
    guided by a warm and careful approach to each story.<br>
    Our sessions help you understand feelings, ease anxiety<br>
    and build steadier ways to face daily life and its changes.<br>
    Each process is shaped to your needs and your own pace,<br>
    with respect, confidentiality and ethical commitment.<br>
    Sessions happen at the clinic or online, wherever you are.<br>
    Book a first conversation and take the first step today.</p>
  </section>

  <aside class="panel portrait-panel">
    <div class="photo-frame" role="img" aria-label="Portrait of the therapist"></div>
    <p class="therapist-name">Dra. Clara Venturi</p>
    <p class="therapist-role">Clinical Psychologist</p>
  </aside>

  <section class="panel feature-panel">
    <div class="feature-strip">ONLINE TREATMENT</div>
    <div class="photo-frame" role="img" aria-label="Image of an online therapy session"></div>
    <p class="body-copy">Online treatment brings the same care of the clinic to you.<br>
    Meet your therapist by secure video from home or work,<br>
    with flexible hours that fit your routine and your time.<br>
    All you need is a quiet place and a stable connection.<br>
    Sessions keep full privacy and follow ethical guidelines.<br>
    <a href="#" class="cta-link">Online Treatment, click here</a> to book your first session.</p>
  </section>
</body>
</html>
```